Brochure Design

Looking for a sharp-looking brochure to provide to managers and customers. We have a ton of pictures, so please reach out if you need more! Or get some off google, haha.
www.tindaleyardworks.com

We provide these services below:

- Seal Coating
- Striping
- Crack Filling
- Paving
- Concrete
- Wheel blocks
- Sign installation
- 24 hour water break service
- Power Washing
- Commercial Curbing
- Bollard installation
- Thermoplastic
- Gas station pump area steam cleaning
- Street Sweeping
- Grading
- Material Delivery

This will be a 8" x 11" TRI FOLD BROCHURE. I will need to be able to upload it to ondell press.

```html
<!DOCTYPE html>
<html lang="en">
<head>
<meta charset="utf-8">
<title>Tindale Yardworks – Tri-fold Brochure</title>
<link rel="stylesheet" href="https://fonts.googleapis.com/css2?family=Montserrat:wght@600;700;800&family=Arimo:wght@400;700&display=swap">
<style>
:root{
  --blue:#2a74e0;
  --blue-deep:#1d5fc4;
  --ink:#4a4d52;
  --black:#0b0b0c;
  --paper:#ffffff;
  --stage:#e4e4e4;
  --sky:#4f87d1;
  --asphalt:#2a2b2e;
  --grass:#5f8f3c;
}
*{box-sizing:border-box;margin:0;padding:0}
html,body{width:917px;height:1200px;overflow:hidden}
body{background:var(--stage);font-family:"Arimo",Arial,sans-serif;color:var(--ink);position:relative}
.spread{position:absolute;left:88px;width:741px;height:572px;display:grid;grid-template-columns:repeat(3,247px);background:var(--paper);box-shadow:0 4px 14px rgba(0,0,0,.18)}
.spread--outside{top:18px}
.spread--inside{top:610px}
.panel{position:relative;overflow:hidden;display:flex;flex-direction:column}
.panel--dark{background:var(--black)}
.band{position:absolute;left:0;right:0;bottom:0;height:38px;background:var(--blue);color:#fff;display:flex;align-items:center;justify-content:center;font-family:"Montserrat",sans-serif;font-weight:600;font-size:12.5px;white-space:nowrap}
.band--phone{font-size:19px;font-weight:800;letter-spacing:.5px}
.photo{position:relative}
.tab{display:inline-block;background:var(--blue);color:#fff;font-family:"Arimo",sans-serif;font-weight:700;border-radius:2px 8px 2px 2px}
.body-copy{font-size:7.6px;line-height:1.32;color:var(--ink)}
.body-copy p+p{margin-top:6px}
.brand{display:flex;align-items:center;justify-content:center;gap:8px;color:#fff;font-family:"Montserrat",sans-serif;font-weight:700;font-size:17px}
.brand-dot{width:12px;height:12px;border-radius:50%;background:#fff}
/* outside spread */
.about-photo{height:218px;background:linear-gradient(160deg,#6fa1d8 0%,#4d7a3e 30%,#2d2e31 60%,#3b3d40 100%)}
.swoosh{position:absolute;left:0;top:170px;width:247px;height:70px}
.about-tab{position:absolute;left:14px;top:214px;font-size:14px;padding:3px 36px 3px 10px}
.about-copy{position:absolute;left:14px;right:12px;top:246px}
.back-photo{height:300px;background:linear-gradient(180deg,#4d86d3 0%,#8fb4e0 22%,#6c7276 48%,#2b2c2e 75%,var(--black) 100%)}
.back-brand{position:absolute;left:0;right:0;top:368px;flex-direction:column;gap:10px}
.back-brand .brand-dot{width:54px;height:54px;background:none;border:3px solid #fff}
.cover-head{padding:22px 16px 0;color:var(--blue);font-family:"Montserrat",sans-serif;font-weight:800;font-size:11px;line-height:1.3;text-transform:uppercase;text-align:center}
.cover-copy{padding:8px 20px 0;text-align:center;font-size:8px;line-height:1.35}
.cover-photo-a{position:absolute;left:0;right:0;top:122px;height:210px;background:linear-gradient(150deg,#c9c3b9 0%,#9a4b3c 35%,#2e4f9b 60%,#5a5d62 100%)}
.cover-photo-b{position:absolute;left:0;right:0;top:332px;height:202px;background:linear-gradient(170deg,#4f7f3a 0%,#8a8d88 45%,#b9bbb8 100%)}
.cover-curves{position:absolute;left:0;top:100px;width:247px;height:260px}
/* inside spread */
.services{padding:18px 14px 0}
.services-tab{font-size:22px;padding:2px 22px;width:100%;text-align:center}
.service-grid{display:grid;grid-template-columns:1fr 1fr;column-gap:10px;row-gap:11px;margin-top:10px}
.service h3{font-family:"Arimo",sans-serif;font-weight:700;font-size:10px;color:#5b5e63;margin-bottom:5px;white-space:nowrap}
.service h3.small{font-size:8px}
.service h3::before{content:"";display:inline-block;width:4px;height:4px;border-radius:50%;background:var(--blue);margin:0 4px 2px 2px}
.thumb{height:58px;border:2px solid var(--blue);border-radius:6px}
.center-photo{height:330px;background:linear-gradient(180deg,#4f86d1 0%,#8eb2df 25%,#b7ad94 40%,#6f7a4a 55%,#2b2c2f 80%,var(--black) 100%)}
.center-brand{position:absolute;left:0;right:0;top:380px;flex-direction:column;gap:10px}
.center-brand .brand-dot{width:58px;height:58px;background:none;border:3px solid #fff}
.map{position:absolute;left:10px;right:10px;top:470px;height:60px;border-radius:6px;background:linear-gradient(135deg,#eef0f2,#dfe3e7)}
.striping{padding:26px 14px 0 14px}
.striping-tab{font-size:13px;padding:4px 12px}
.striping-copy{margin-top:14px;font-size:7.8px;line-height:1.35}
.striping-photo{position:absolute;left:0;right:0;top:150px;bottom:38px;background:linear-gradient(180deg,#f3f5f8 0%,#a9c1a0 18%,#6b8a4a 40%,#9a5a44 55%,#3a3c3f 75%,#222326 100%)}
</style>
</head>
<body>

<section class="spread spread--outside" aria-label="Brochure outside">
  <article class="panel panel--about">
    <div class="photo about-photo" role="img" aria-label="Worker in a hi-vis shirt spraying sealcoat on a parking lot"></div>
    <svg class="swoosh" viewBox="0 0 247 70" aria-hidden="true">
      <path d="M0 40 Q120 0 247 52 L247 70 L0 70Z" fill="#fff"/>
      <path d="M0 36 Q120 -4 247 48" fill="none" stroke="var(--blue)" stroke-width="5"/>
      <path d="M0 44 Q120 6 247 56" fill="none" stroke="var(--blue)" stroke-width="1.5"/>
    </svg>
    <h2 class="tab about-tab">About Us</h2>
    <div class="about-copy body-copy">
      <p>Tindale Yardworks is a full service parking lot maintenance and power washing company with over 10 years of providing outstanding service in the region. As a fully licensed and insured company we are now taking our expertise and expanding into the northern Idaho region.</p>
      <p>At Tindale Yardworks, we believe that first impressions are everything. Your parking lot area is your first physical interaction with the customer. Professional line striping is an effective and economical way to greatly enhance the curb appeal of your business and make it more inviting to customers. Many business owners and their customers agree that a parking lot should look clean, inviting and be easy to navigate. Please allow us to help you achieve that goal. We provide professional line striping and related services using top quality equipment and materials, at reasonable costs.</p>
      <p>We offer complete layout and line striping services using the best striping equipment and quality paint available. Our superior service is well known by general contractors as well as municipal and commercial building owners and numerous churches throughout the region. We offer competitive quotes and work to complete the job promptly and on time.</p>
    </div>
    <div class="band">www.tindaleyardworks.com</div>
  </article>

  <article class="panel panel--dark">
    <div class="photo back-photo" role="img" aria-label="Crew striping a parking lot under a blue sky"></div>
    <div class="brand back-brand"><span class="brand-dot"></span><span>Tindale Yardworks</span></div>
    <div class="band">418 Orchard Road, Larkfield, ID 83000</div>
  </article>

  <article class="panel panel--cover">
    <h1 class="cover-head">Parking lot striping &amp; sealcoating, crack filling, repairs &amp; maintenance.</h1>
    <p class="cover-copy">Tindale Yardworks is a leader in parking lot maintenance in northern Idaho and eastern Washington.</p>
    <div class="cover-photo-a" role="img" aria-label="Line striping machine in front of a storefront"></div>
    <div class="cover-photo-b" role="img" aria-label="Crew painting new parking lines"></div>
    <svg class="cover-curves" viewBox="0 0 247 260" aria-hidden="true">
      <path d="M0 22 Q140 -6 247 30 L247 0 L0 0Z" fill="#fff"/>
      <path d="M0 24 Q140 -4 247 32" fill="none" stroke="var(--black)" stroke-width="2"/>
      <path d="M0 228 Q130 210 247 250 L247 260 L0 260Z" fill="var(--blue)" opacity=".9"/>
      <path d="M0 238 Q130 222 247 258" fill="none" stroke="#fff" stroke-width="2"/>
    </svg>
    <div class="band band--phone">1-800-555-0147</div>
  </article>
</section>

<section class="spread spread--inside" aria-label="Brochure inside">
  <article class="panel">
    <div class="services">
      <h2 class="tab services-tab">Our Services</h2>
      <div class="service-grid">
        <div class="service"><h3>Striping</h3><div class="thumb" role="img" aria-label="Fresh white line on black asphalt" style="background:linear-gradient(160deg,#4a6c8a,#1e2a38)"></div></div>
        <div class="service"><h3>Sealcoating</h3><div class="thumb" role="img" aria-label="Sealed lot beside autumn trees" style="background:linear-gradient(180deg,#b27a52,#4f7a3c 55%,#2a2b2e)"></div></div>
        <div class="service"><h3 class="small">Commercial Curbing</h3><div class="thumb" role="img" aria-label="New curbing taped off at a storefront" style="background:linear-gradient(160deg,#8a5a3c,#2d3a48 60%,#c9b23a)"></div></div>
        <div class="service"><h3>Asphalt Repair</h3><div class="thumb" role="img" aria-label="Steam rising from hot asphalt patch" style="background:linear-gradient(160deg,#9fb3c2,#4a5560)"></div></div>
        <div class="service"><h3 class="small">Concrete Services</h3><div class="thumb" role="img" aria-label="Workers pouring concrete" style="background:linear-gradient(160deg,#5f7d4a,#7a7a76 60%,#3b3d40)"></div></div>
        <div class="service"><h3 class="small">Residential Curbing</h3><div class="thumb" role="img" aria-label="Curved garden curbing on a lawn" style="background:linear-gradient(160deg,#6fa34a,#3f6b2c 70%,#8a5a44)"></div></div>
        <div class="service"><h3>Crack Filling</h3><div class="thumb" role="img" aria-label="Crack sealant applied to pavement" style="background:linear-gradient(160deg,#b5aea4,#6a6660)"></div></div>
        <div class="service"><h3 class="small">Pressure Washing</h3><div class="thumb" role="img" aria-label="Worker pressure washing a driveway" style="background:linear-gradient(180deg,#5f8a4a,#a8b0b6 60%,#d3d6d8)"></div></div>
      </div>
    </div>
    <div class="band">www.tindaleyardworks.com</div>
  </article>

  <article class="panel panel--dark">
    <div class="photo center-photo" role="img" aria-label="Newly sealed apartment complex parking lot"></div>
    <div class="brand center-brand"><span class="brand-dot"></span><span>Tindale Yardworks</span></div>
    <div class="map" role="img" aria-label="Street map showing the office location"></div>
    <div class="band">418 Orchard Road, Larkfield, ID 83000</div>
  </article>

  <article class="panel">
    <div class="striping">
      <h2 class="tab striping-tab">Professional Line Striping</h2>
      <p class="striping-copy">We offer complete layout and line striping services using the best striping equipment and quality paint available. Our superior service is well known by general contractors as well as municipal and commercial building owners and numerous churches throughout the northwest. We offer competitive quotes and work to complete the job promptly and on time.</p>
    </div>
    <div class="striping-photo" role="img" aria-label="Freshly sealed office lot framed by evergreen and autumn trees"></div>
    <div class="band band--phone">1-800-555-0147</div>
  </article>
</section>

</body>
</html>
```